Web Design Project

we require new design / layout for www.brimlodge.eu design clean easy read must send strong and industrial theme as selling point to our product is the strength in our products

To include step process for the www.brimlodge.eu/designer2

For step process have similar layout to http://www.thewaxgarden.com/create/own_temp.php

Industry/Entity Type

Industrial

```html
<!DOCTYPE html>
<html lang="en">
<head>
<meta charset="utf-8">
<title>Brimlodge – Pop Up Gazebos</title>
<link href="https://fonts.googleapis.com/css2?family=Michroma&family=Questrial&family=Arimo:wght@400;700&display=swap" rel="stylesheet">
<style>
  :root{
    --red:#e41b17;
    --navy:#1a2e8c;
    --navy-dark:#14258a;
    --ink:#333;
    --muted:#777;
    --line:#d9d9d9;
    --band:#e6e6e6;
    --white:#fff;
  }
  *{box-sizing:border-box;margin:0;padding:0}
  html,body{width:886px;height:1200px;overflow:hidden;background:var(--white)}
  body{position:relative;font-family:"Arimo",Arial,sans-serif;color:var(--ink)}
  .abs{position:absolute}
  .page{position:absolute;left:63px;top:0;width:760px;height:1200px;background:var(--white);box-shadow:0 0 4px rgba(0,0,0,.15)}

  /* header */
  .brand{left:105px;top:30px;display:flex;align-items:center;gap:6px;font-family:"Questrial",sans-serif;font-size:17px;color:var(--red);font-weight:400}
  .brand-mark{width:10px;height:10px;background:var(--red)}
  .nav a{position:absolute;top:26px;font-family:"Questrial",sans-serif;font-size:15px;color:var(--navy);text-decoration:none}
  .nav-tab{left:361px;top:0;width:94px;height:78px}
  .nav a.active{color:var(--white);top:26px;left:372px}
  .tollfree{display:inline-flex;align-items:center;gap:3px;background:var(--red);color:var(--white);font-size:9px;padding:1px 5px;border-radius:2px;font-family:"Arimo",sans-serif}
  .phone{font-family:"Questrial",sans-serif;color:#111;font-size:15.5px;letter-spacing:.3px}

  /* hero */
  .hero{left:63px;top:66px;width:760px;height:398px;background:linear-gradient(180deg,#8ea3b4 0%,#c7cdd0 35%,#d9d9d4 52%,#6f7a4c 70%,#4f6a2a 100%)}
  .hero-title{left:105px;top:253px;font-family:"Michroma",sans-serif;font-size:23px;line-height:27px;color:var(--white);text-shadow:0 1px 3px rgba(0,0,0,.5)}
  .hero-panel{left:105px;top:311px;width:360px;height:97px;background:rgba(26,46,140,.82)}
  .hero-list{position:absolute;list-style:none;color:var(--white);font-size:12.5px}
  .hero-list li{display:flex;align-items:center;gap:9px;height:22px}
  .go{display:flex;align-items:center;justify-content:center;background:var(--red)}
  .thumb{left:470px;width:30px;height:30px;border:1px solid #ccc}
  .hero-arrow{top:214px;width:28px;height:56px;background:rgba(255,255,255,.55)}
  .account{left:520px;top:441px;width:303px;height:23px;background:var(--white);clip-path:polygon(14px 0,100% 0,100% 100%,0 100%);font-size:10px;color:var(--muted);letter-spacing:.4px}
  .account span{position:absolute;top:6px}

  /* intro */
  .section-title{left:85px;top:496px;width:720px;text-align:center;font-family:"Questrial",sans-serif;font-size:16px;color:var(--navy)}
  .intro{left:90px;top:527px;width:686px;text-align:center;font-size:9.8px;line-height:12px;color:#444}

  /* products */
  .product{top:600px;width:123px}
  .product .img{width:123px;height:123px}
  .product p{margin-top:11px;text-align:center;font-size:10px;line-height:12px;color:#666}
  .price{position:absolute;left:0;bottom:0;width:123px;height:29px;background:var(--red);color:var(--white);font-size:14px;display:flex;align-items:center;justify-content:center}
  .chev{top:655px;color:#555}

  /* feature tiles */
  .tile{top:782px;height:75px;color:var(--white);font-family:"Michroma",sans-serif}
  .tile h3{position:absolute;font-weight:400;font-size:12px;line-height:16px}
  .notch{position:absolute;top:0;width:0;height:0;border-left:8px solid transparent;border-right:8px solid transparent;border-top:8px solid var(--white)}

  /* band */
  .band{left:58px;top:888px;width:770px;height:147px;background:var(--band)}
  .pay-title{left:689px;top:906px;font-family:"Questrial",sans-serif;font-size:13px;line-height:16px;color:#222}
  .card{width:44px;height:26px;border-radius:2px}

  /* footer */
  .links{list-style:none;font-size:9px;line-height:16px;color:#111}
  .contact-title{left:282px;top:1064px;font-family:"Questrial",sans-serif;font-size:14px;color:var(--navy)}
  .field{left:283px;width:161px;height:18px;border:1px solid var(--line);font-size:9px;color:#999;padding:4px 9px}
  .social{width:28px;height:28px;border-radius:50%;background:#b9b9b9}
  .footbar{left:63px;top:1170px;width:760px;height:30px;background:var(--navy-dark);color:#5a6cc0;font-size:9px;text-align:right;padding:11px 41px 0 0}
</style>
</head>
<body>
<div class="page"></div>

<!-- header -->
<div class="abs brand"><span class="brand-mark"></span>brimlodge.eu</div>
<svg class="abs nav-tab" viewBox="0 0 94 78" aria-hidden="true"><polygon points="0,0 94,0 94,66 47,78 0,66" fill="#e41b17"/></svg>
<nav class="nav">
  <a style="left:296px" href="#">Home</a>
  <a class="active" href="#">Products</a>
  <a style="left:474px" href="#">FAQ</a>
  <a style="left:538px" href="#">Contact Us</a>
</nav>
<div class="abs" style="left:644px;top:11px"><span class="tollfree"><svg width="7" height="7" viewBox="0 0 10 10"><path d="M2 0l2 2-1 2 3 3 2-1 2 2-2 2C4 10 0 6 0 2z" fill="#fff"/></svg>TOLLFREE</span></div>
<div class="abs phone" style="left:644px;top:26px">0800 12 34 567</div>

<!-- hero -->
<div class="abs hero" role="img" aria-label="Row of large white peaked marquee tents on a lawn at sunset"></div>
<div class="abs hero-arrow" style="left:63px;border-radius:0 28px 28px 0"></div>
<div class="abs hero-arrow" style="left:795px;border-radius:28px 0 0 28px"></div>
<h1 class="abs hero-title" style="font-weight:400">THE STRONGEST<br>POP TENTS IN THE WORLD</h1>
<div class="abs hero-panel">
  <ul class="hero-list" style="left:26px;top:6px">
    <li><svg width="11" height="11" viewBox="0 0 12 12"><circle cx="6" cy="6" r="6" fill="#fff"/><path d="M3 6l2 2 4-4" stroke="#1a2e8c" stroke-width="1.6" fill="none"/></svg>Heavy Duty</li>
    <li><svg width="11" height="11" viewBox="0 0 12 12"><circle cx="6" cy="6" r="6" fill="#fff"/><path d="M3 6l2 2 4-4" stroke="#1a2e8c" stroke-width="1.6" fill="none"/></svg>Carry Bag</li>
    <li><svg width="11" height="11" viewBox="0 0 12 12"><circle cx="6" cy="6" r="6" fill="#fff"/><path d="M3 6l2 2 4-4" stroke="#1a2e8c" stroke-width="1.6" fill="none"/></svg>Heavy Pegs/Staps</li>
  </ul>
  <ul class="hero-list" style="left:168px;top:6px">
    <li><svg width="11" height="11" viewBox="0 0 12 12"><circle cx="6" cy="6" r="6" fill="#fff"/><path d="M3 6l2 2 4-4" stroke="#1a2e8c" stroke-width="1.6" fill="none"/></svg>Complete with 4 Walls</li>
    <li><svg width="11" height="11" viewBox="0 0 12 12"><circle cx="6" cy="6" r="6" fill="#fff"/><path d="M3 6l2 2 4-4" stroke="#1a2e8c" stroke-width="1.6" fill="none"/></svg>Quick Delivery</li>
    <li><svg width="11" height="11" viewBox="0 0 12 12"><circle cx="6" cy="6" r="6" fill="#fff"/><path d="M3 6l2 2 4-4" stroke="#1a2e8c" stroke-width="1.6" fill="none"/></svg>100% Waterproof</li>
  </ul>
  <div class="abs go" style="left:323px;top:67px;width:37px;height:30px"><svg width="16" height="16" viewBox="0 0 16 16"><circle cx="8" cy="8" r="8" fill="#fff"/><path d="M4 8h6M8 5l3 3-3 3" stroke="#e41b17" stroke-width="1.8" fill="none"/></svg></div>
</div>
<div class="abs thumb" style="top:311px;background:linear-gradient(#9fb0be,#d8d8d2 60%,#5d7030)" role="img" aria-label="Marquee thumbnail"></div>
<div class="abs thumb" style="top:344px;background:linear-gradient(#b8c4cc,#e6e3d8 60%,#6b7a3a)" role="img" aria-label="Marquee thumbnail"></div>
<div class="abs thumb" style="top:377px;background:linear-gradient(#2c3f7c,#5d6fa8 60%,#2b3550)" role="img" aria-label="Marquee at night thumbnail"></div>
<div class="abs account">
  <span style="left:18px">MY ACCOUNT</span>
  <span style="left:98px;color:#444"><svg width="11" height="9" viewBox="0 0 12 10"><path d="M0 1h2l2 6h6l1-4H3" stroke="#555" fill="none" stroke-width="1.3"/><circle cx="5" cy="9" r="1" fill="#555"/><circle cx="9" cy="9" r="1" fill="#555"/></svg> SHOPPING CART</span>
  <span style="left:217px;top:5px;background:#e3e3e3;padding:1px 4px;font-size:8.5px">▾ US</span>
</div>

<!-- intro -->
<svg class="abs" style="left:85px;top:503px" width="720" height="10" aria-hidden="true">
  <line x1="0" y1="5" x2="720" y2="5" stroke="#e2e2e2"/>
  <polygon points="210,5 245,2 245,8" fill="#1a2e8c"/><polygon points="510,5 475,2 475,8" fill="#1a2e8c"/>
</svg>
<h2 class="abs section-title" style="font-weight:400"><span style="background:#fff;padding:0 8px">Pop Up Gazebos For Sale</span></h2>
<p class="abs intro">Pop up gazebos for sale near you! We at Brimlodge have been able to expand our markets to different countries and our pop up gazebos are now available for delivery in several European countries, so your wait is over. All you have to do now is order your instant awnings from our website Brimlodge.eu Please note that we deliver to the UK , Ireland, Europe <svg width="8" height="8" viewBox="0 0 8 8"><circle cx="4" cy="4" r="4" fill="#e41b17"/><path d="M2 4h3M4 2.5L5.5 4 4 5.5" stroke="#fff" fill="none"/></svg></p>

<!-- products -->
<div class="abs chev" style="left:81px">❮</div>
<div class="abs chev" style="left:796px">❯</div>
<div class="abs product" style="left:105px"><div class="img" role="img" aria-label="White pop up gazebo with walls" style="background:linear-gradient(#eef0f1 0%,#d7dadc 70%,#7a8a58 100%)"></div><p>Extreme Series White<br>3m x 3m</p></div>
<div class="abs product" style="left:243px"><div class="img" role="img" aria-label="Blue pop up gazebo with walls" style="position:relative;background:linear-gradient(#8fc7ee 0%,#2f5fd0 25%,#2148b8 80%,#6e7f56 100%)">
  <svg style="position:absolute;left:53px;top:59px" width="17" height="17" viewBox="0 0 16 16"><circle cx="8" cy="8" r="8" fill="#fff"/><path d="M4 8h6M8 5l3 3-3 3" stroke="#2148b8" stroke-width="1.8" fill="none"/></svg>
  <div class="price">£307.50 + VAT</div></div><p>Extreme Series Blue<br>3m x 3m</p></div>
<div class="abs product" style="left:381px"><div class="img" role="img" aria-label="Orange pop up gazebo with walls" style="background:linear-gradient(#f7b04a 0%,#f08a1c 30%,#ea7a10 85%,#9a8f70 100%)"></div><p>Extreme Series<br>3m x 3m</p></div>
<div class="abs product" style="left:520px"><div class="img" role="img" aria-label="White 3 by 4.5 metre gazebo on grass" style="background:linear-gradient(#6d7c5a 0%,#e6e8e8 25%,#cfd2d2 70%,#4f5d2e 100%)"></div><p>Extreme Series White<br>3m x 4.5m</p></div>
<div class="abs product" style="left:658px"><div class="img" role="img" aria-label="Long white 3 by 6 metre gazebo in a park" style="background:linear-gradient(#8fa6c4 0%,#c8d3de 35%,#e8e8e4 55%,#5a6e30 80%,#3e5222 100%)"></div><p>Extreme Series Blue<br>3m x 6m</p></div>

<!-- feature tiles -->
<div class="abs tile" style="left:105px;width:221px;background:linear-gradient(90deg,#3a3f46,#6b737d 60%,#8c939b)">
  <div role="img" aria-label="Padlock shield emblem" style="position:absolute;left:21px;top:10px;width:50px;height:56px;background:var(--red);border-radius:6px 6px 25px 25px"></div>
  <span class="notch" style="left:107px"></span>
  <h3 style="left:86px;top:22px">100% SECURE<br>SHOPPING</h3>
</div>
<div class="abs tile" style="left:332px;width:222px;background:linear-gradient(135deg,#2a4fa8,#4a6fc4 70%,#5a7ac8)">
  <span class="notch" style="left:103px"></span>
  <h3 style="left:10px;top:20px">WHY BUY FROM US</h3>
  <p style="position:absolute;left:10px;top:37px;font-family:'Arimo',sans-serif;font-size:9.5px;line-height:12px">Lorem ipsum dolor sit amet consectetur amet<br>Adipisicing elit amet, consectetur</p>
</div>
<div class="abs tile" style="left:559px;width:222px;background:linear-gradient(90deg,#b0a690,#9d937c)">
  <div role="img" aria-label="White peaked marquee photo" style="position:absolute;left:0;top:0;width:82px;height:75px;background:linear-gradient(#a8c0d8,#e4e4e0 55%,#6e7a56)"></div>
  <span class="notch" style="left:82px;border-top-color:#fff"></span>
  <h3 style="left:100px;top:22px">DESIGN YOUR<br>OWN TENT</h3>
  <svg style="position:absolute;left:193px;top:51px" width="16" height="16" viewBox="0 0 16 16"><circle cx="8" cy="8" r="8" fill="#fff"/><path d="M4 8h6M8 5l3 3-3 3" stroke="#9d937c" stroke-width="1.8" fill="none"/></svg>
</div>

<!-- band -->
<div class="abs band"></div>
<div class="abs" role="img" aria-label="Promotional banner: our frames are strong enough to hang a car from" style="left:105px;top:909px;width:570px;height:98px;background:linear-gradient(90deg,#2a2a2a,#5a5a5a 45%,#1e1e1e 65%,#111)"></div>
<div class="abs pay-title">Payment and<br>Security with</div>
<div class="abs card" style="left:689px;top:947px;background:#f4f4f4"></div>
<div class="abs card" style="left:737px;top:947px;background:#f4f4f4"></div>
<div class="abs card" style="left:689px;top:976px;background:#1d3a8a"></div>
<div class="abs card" style="left:737px;top:976px;background:#1d3a8a"></div>

<!-- footer -->
<ul class="abs links" style="left:105px;top:1066px"><li>Home</li><li>FAQ</li><li>About Us</li><li>Instructions</li><li>Privacy</li></ul>
<ul class="abs links" style="left:172px;top:1066px"><li>Delivery</li><li>ayment &amp; Returns</li><li>Terms &amp; Conditions</li><li>Contact Us</li><li>Tent Templates</li></ul>
<div class="abs contact-title">CONTACT US</div>
<div class="abs field" style="top:1087px">Your name</div>
<div class="abs field" style="top:1108px">Email</div>
<div class="abs field" style="top:1130px">Phone</div>
<div class="abs field" style="left:448px;top:1087px;width:150px;height:61px">Message</div>
<div class="abs go" style="left:597px;top:1087px;width:37px;height:61px;flex-direction:column;gap:5px;color:#fff;font-size:8.5px"><svg width="15" height="15" viewBox="0 0 16 16"><circle cx="8" cy="8" r="8" fill="#fff"/><path d="M4 8h6M8 5l3 3-3 3" stroke="#e41b17" stroke-width="1.8" fill="none"/></svg>Send</div>
<div class="abs" style="left:653px;top:1089px"><span class="tollfree"><svg width="7" height="7" viewBox="0 0 10 10"><path d="M2 0l2 2-1 2 3 3 2-1 2 2-2 2C4 10 0 6 0 2z" fill="#fff"/></svg>TOLLFREE</span></div>
<div class="abs phone" style="left:653px;top:1103px;color:var(--navy)">0800 12 34 567</div>
<div class="abs social" style="left:651px;top:1123px"></div>
<div class="abs social" style="left:684px;top:1123px"></div>
<div class="abs social" style="left:717px;top:1123px"></div>
<div class="abs social" style="left:751px;top:1123px"></div>
<div class="abs footbar">All Right Reserved © 2013</div>
</body>
</html>
```